Modern Catering Company needs Letterhead Design

We need a letterhead design that will make effective use of the corporate logo and color scheme, along with careful typography, helps this letterhead design communicate the brand well. We do have a corporate logo, however feel free to enhance the color scheme with gold and purple. We are serving a very upscale clientele so the letterhead has to reflect elegance, professionalism, cleanliness, and modern style. We are branding the company so the letterhead and business cards must fit the brand story. There should be no cartoonish elements in the design and we are looking for sharper lines.

Target Market(s)

Businesses and upscale clientele

Industry/Entity Type

Catering

Contact Information for Business Card

while this design can have any number of quirks and distinctions, it needs to be cohesive with the entire brand story clean, professional but edgy

Requirements
Must have
• must have good and carefully placement of it’s logo and where you place the text or the message. Colors blue, very deep purple, jewel tones not pastels, gold. Blue must be the primary color you may accent with purple or gold. Contact information is as follows: Co-Owners/ Chefs: R. Hollowmere & L. Brandt, phone: 414-555-0182 email:Contact@orchardtablecatering.example, address: 6127 W Larkspur Hollow Rd, Milwaukee, WI 53299
Should not have
• pastel colors, Do not add the BBQ information to the letterhead or business card it was a mistake by the previous designer.

```html
<!DOCTYPE html>
<html lang="en">
<head>
<meta charset="utf-8">
<title>Orchard Table Catering – Business Card</title>
<link href="https://fonts.googleapis.com/css2?family=Source+Sans+3:wght@400;600&display=swap" rel="stylesheet">
<style>
  :root {
    --stage-top: #2b2b2b;
    --stage-bottom: #050505;
    --card-light: #e7e7e7;
    --brand-blue: #0a6cf0;
    --ink: #2b2b2b;
    --white: #ffffff;
  }
  html, body {
    margin: 0;
    width: 1200px;
    height: 900px;
    overflow: hidden;
  }
  body {
    position: relative;
    background: radial-gradient(ellipse at 50% 20%, var(--stage-top) 0%, #161616 55%, var(--stage-bottom) 100%);
    font-family: "Source Sans 3", "Myriad Pro", Arial, sans-serif;
  }
  .card {
    position: absolute;
    top: 184px;
    width: 302px;
    height: 490px;
    border-radius: 12px;
    overflow: hidden;
  }
  .card--front {
    left: 299px;
    background: var(--card-light);
    color: var(--ink);
    text-align: center;
  }
  .card--back {
    left: 646px;
    width: 303px;
    background: var(--brand-blue);
  }

  /* wordmark – single colour, single weight */
  .wordmark {
    position: absolute;
    margin: 0;
    font-weight: 400;
    line-height: 1;
    text-transform: uppercase;
  }
  .wordmark__line { display: block; }
  .wordmark__line--main { font-size: 34px; letter-spacing: 0.5px; }
  .wordmark__line--sub { font-size: 24px; letter-spacing: 10px; margin-top: 8px; }

  .card--front .brand-dot {
    position: absolute;
    left: 131px;
    top: 44px;
    width: 40px;
    height: 40px;
    border-radius: 50%;
    background: var(--brand-blue);
  }
  .card--front .wordmark {
    left: 0;
    right: 0;
    top: 122px;
    color: var(--brand-blue);
  }
  .card--front .wordmark__line--sub { margin-right: -10px; }
  .card--back .wordmark {
    right: 26px;
    top: 346px;
    text-align: right;
    color: var(--white);
  }
  .card--back .wordmark__line--main { font-size: 36px; }
  .card--back .wordmark__line--sub { margin-right: -10px; }

  .person {
    position: absolute;
    left: 0;
    right: 0;
    top: 270px;
  }
  .person__name {
    margin: 0;
    font-size: 17px;
    font-weight: 600;
    color: var(--brand-blue);
    text-transform: uppercase;
    letter-spacing: 0.2px;
  }
  .person__role {
    margin: 4px 0 0;
    font-size: 14.5px;
  }
  .contact {
    position: absolute;
    left: 0;
    right: 0;
    top: 342px;
    margin: 0;
    padding: 0;
    list-style: none;
    font-size: 13.5px;
    line-height: 20px;
  }
  .contact__item {
    display: flex;
    align-items: center;
    justify-content: center;
    gap: 8px;
  }
  .contact__icon { width: 11px; height: 11px; fill: var(--brand-blue); flex: none; }
  .address {
    position: absolute;
    left: 0;
    right: 0;
    top: 420px;
    margin: 0;
    font-style: normal;
    font-size: 14px;
    line-height: 17px;
  }
</style>
</head>
<body>
  <section class="card card--front" aria-label="Business card front">
    <span class="brand-dot" aria-hidden="true"></span>
    <h1 class="wordmark">
      <span class="wordmark__line wordmark__line--main">Orchard Table</span>
      <span class="wordmark__line wordmark__line--sub">Catering</span>
    </h1>

    <div class="person">
      <p class="person__name">R. Hollowmere &amp; L. Brandt</p>
      <p class="person__role">Co-Owners / Chefs</p>
    </div>

    <ul class="contact">
      <li class="contact__item">
        <svg class="contact__icon" viewBox="0 0 12 12" aria-hidden="true">
          <path d="M1 4.5C1 2.5 3 1.5 6 1.5S11 2.5 11 4.5L8.6 5.2 8.2 3.9H3.8L3.4 5.2ZM3.2 6H8.8L10 10.5H2Z"/>
        </svg>
        <span>414-555-0182</span>
      </li>
      <li class="contact__item">
        <svg class="contact__icon" viewBox="0 0 12 12" aria-hidden="true">
          <path d="M1 2.5H11V3.4L6 6.6 1 3.4ZM1 4.6L6 7.8 11 4.6V9.5H1Z"/>
        </svg>
        <span>Contact@orchardtablecatering.example</span>
      </li>
    </ul>

    <address class="address">
      6127 W Larkspur Hollow Rd,<br>
      Milwaukee, WI 53299
    </address>
  </section>

  <section class="card card--back" aria-label="Business card back">
    <p class="wordmark">
      <span class="wordmark__line wordmark__line--main">Orchard Table</span>
      <span class="wordmark__line wordmark__line--sub">Catering</span>
    </p>
  </section>
</body>
</html>
```